Real Estate Company Looking for Business Card Designs for 3 Executives

Hello!
Thanks so much for considering our project! We are a real estate investment company located in Edmonton, Alberta called Marlbeck Group of Companies. We invest/develop both commercial and residential real estate and are looking to create 3 DOUBLE-SIDED business cards for 3 top executives in the company! (for some reason it won't let us select the double-sided option, but yes, the cards are double sided and would be happy to tip extra)

We have certain guidelines that we want our business cards to for sure follow - the back of the Business card has to be the Black Background Version of the Logo which has already been designed and linked as a file (first file). We want the entire back of the card to simply just be the black background logo. In terms of the front of the card, would like to see a smaller version of the white background logo (linked as the second file) in the top left hand corner - of course, feel free to get creative and we can make revisions together along the way! and Then after that, just text. We want the card to be sharp, clean, easy on the eyes and highly professional looking. We would like the card to include the Full name of the Company (Marlbeck Group of Companies), Name of the Person, Title, Phone, Email. If possible please provide the front part of the card for 3 people:

1) Marlbeck Group of Companies, Lena Okafor, Chief Financial Officer, 780-555-0162, lenaokafor@marlbeckgroup.example

2) Marlbeck Group of Companies, Tobias Okafor, Chief Executive Officer, 780-555-0148, tobiasokafor@marlbeckgroup.example

3) Marlbeck Group of Companies, Rui Dalton, Chief Operations Officer, 587-555-0193, ruidalton@marlbeckgroup.example

Thank you so much for considering our project & we look forward to seeing your designs!

```html
<!DOCTYPE html>
<html lang="en">
<head>
<meta charset="utf-8">
<title>Marlbeck Group of Companies – Business Card</title>
<link rel="stylesheet" href="https://fonts.googleapis.com/css2?family=Barlow+Condensed:wght@300;400;600&family=Barlow+Semi+Condensed:wght@600&display=swap">
<style>
  :root {
    --ink: #0b0b0b;
    --paper: #ffffff;
    --rule: #111111;
  }
  html, body {
    margin: 0;
    padding: 0;
    width: 1200px;
    height: 686px;
    overflow: hidden;
    background: var(--paper);
  }
  .card {
    position: relative;
    width: 1200px;
    height: 686px;
    box-sizing: border-box;
    border: 1px solid var(--ink);
    background: var(--paper);
    color: var(--ink);
    font-family: "Barlow Condensed", "Arial Narrow", sans-serif;
    overflow: hidden;
  }
  .brand {
    position: absolute;
    left: 146px;
    top: 200px;
    margin: 0;
    font-family: "Barlow Semi Condensed", "Arial Narrow", sans-serif;
    font-weight: 600;
    font-size: 64px;
    line-height: 1;
    letter-spacing: 0.12em;
    color: var(--ink);
  }
  .holder-name {
    position: absolute;
    left: 146px;
    top: 398px;
    margin: 0;
    font-family: "Barlow Semi Condensed", "Arial Narrow", sans-serif;
    font-weight: 600;
    font-size: 46px;
    line-height: 1;
  }
  .holder-title {
    position: absolute;
    left: 147px;
    top: 468px;
    margin: 0;
    font-weight: 400;
    font-size: 28px;
    line-height: 1;
  }
  .divider {
    position: absolute;
    left: 456px;
    top: 411px;
    width: 2px;
    height: 90px;
    background: var(--rule);
  }
  .contact {
    position: absolute;
    left: 532px;
    top: 408px;
    margin: 0;
    padding: 0;
    list-style: none;
  }
  .contact-item {
    display: flex;
    align-items: center;
    height: 40px;
    margin-bottom: 14px;
    font-weight: 300;
    font-size: 38px;
    line-height: 1;
  }
  .contact-icon {
    width: 44px;
    height: 34px;
    margin-right: 18px;
    flex: none;
  }
  .stripe {
    position: absolute;
    left: 0;
    width: 100%;
    background: var(--ink);
  }
  .stripe-top { top: 577px; height: 5px; }
  .stripe-mid { top: 588px; height: 5px; }
  .footer-band {
    position: absolute;
    left: 0;
    top: 606px;
    width: 100%;
    height: 80px;
    background: var(--ink);
    color: var(--paper);
    display: flex;
    align-items: center;
    justify-content: center;
  }
  .company-name {
    margin: 0;
    font-weight: 300;
    font-size: 33px;
    letter-spacing: 0.36em;
    text-transform: uppercase;
    padding-left: 0.36em;
  }
</style>
</head>
<body>
  <main class="card">
    <p class="brand">MARLBECK</p>

    <h1 class="holder-name">Lena Okafor</h1>
    <p class="holder-title">Chief Financial Officer</p>

    <div class="divider" aria-hidden="true"></div>

    <ul class="contact">
      <li class="contact-item">
        <svg class="contact-icon" viewBox="0 0 44 34" aria-hidden="true">
          <path fill="#0b0b0b" d="M9 2 c-3 1 -5 4 -4 9 c2 9 9 17 18 21 c4 1 7 0 8 -3 l1 -3 c0 -1 0 -2 -1 -2 l-6 -3 c-1 0 -2 0 -2 1 l-2 3 c-5 -2 -9 -7 -11 -12 l3 -2 c1 -1 1 -2 1 -3 l-2 -6 c-1 -1 -2 -1 -3 -1 z"/>
        </svg>
        <span>780-555-0162</span>
      </li>
      <li class="contact-item">
        <svg class="contact-icon" viewBox="0 0 44 34" aria-hidden="true">
          <rect x="2" y="5" width="40" height="26" fill="#0b0b0b"/>
          <path d="M3 6 L22 21 L41 6" fill="none" stroke="#ffffff" stroke-width="2.4"/>
          <path d="M3 30 L17 17 M41 30 L27 17" fill="none" stroke="#ffffff" stroke-width="2"/>
        </svg>
        <span>lenaokafor@marlbeckgroup.example</span>
      </li>
    </ul>

    <div class="stripe stripe-top" aria-hidden="true"></div>
    <div class="stripe stripe-mid" aria-hidden="true"></div>
    <footer class="footer-band">
      <p class="company-name">Marlbeck Group of Companies</p>
    </footer>
  </main>
</body>
</html>
```